VORTIQ Business Card Design

We need a business card for a new company based on the Gold Coast, we are a new supplement distributing company called VORTIQ Sports Nutrition - Bold Horizon Sports Nutrition. We are providing new science based bodybuilding and fitness supplementation. Our company has a key focus towards next generation. We are wanting a card that is cool, innovative and fresh. We would like to see the implementation of the below image in a fresh and very innovative design that stands out. The final design should communicate New, Innovative, Cool, Science and researched based.
Target Market(s)
The target market is fitness and bodybuilder enthusiasts. Young audience so very cool looking.
Industry/Entity Type
Fitness
Contact Information for Business Card
(front of card)
VORTIQ Sports Nutrition.
Milo Harrow
CEO/Sport Nutrition Specialist
0473 628 904
Milo@vortiqfuelworks.example
www.vortiqfuelworks.example
(back of card)
Scientifically formulated supplement range
Private Nutrition consultations
comprehensive sports nutrition seminars
Requirements
Nice to have
- The card could have a cut out on one of the sides or one of the corners rounded off so the card looks different from a normal business card.
Should not have
- The colours need to complement each other and pop out.

```html
<!DOCTYPE html>
<html lang="en">
<head>
<meta charset="utf-8">
<title>VORTIQ Sports Nutrition – Business Card</title>
<link rel="stylesheet" href="https://fonts.googleapis.com/css2?family=Arimo:wght@700&family=Open+Sans:ital,wght@1,400&display=swap">
<style>
  :root {
    --page: #ffffff;
    --card-edge: #4383bd;
    --card-mid: #223553;
    --brand-sky: #6cc3e8;
    --text-light: #ffffff;
    --name-red: #a6341c;
    --text-shadow: rgba(0, 0, 0, 0.75);
  }
  html, body {
    margin: 0;
    padding: 0;
    width: 1200px;
    height: 741px;
    overflow: hidden;
    background: var(--page);
  }
  .canvas {
    position: relative;
    width: 1200px;
    height: 741px;
  }
  .card {
    position: absolute;
    left: 54px;
    top: 38px;
    width: 1092px;
    height: 665px;
    border-radius: 32px;
    overflow: hidden;
    background: linear-gradient(180deg,
      var(--card-edge) 0%,
      #2f5885 22%,
      var(--card-mid) 45%,
      #263d60 65%,
      #325e8f 85%,
      var(--card-edge) 100%);
  }
  .card-texture {
    position: absolute;
    inset: 0;
    background: radial-gradient(ellipse at 50% 50%, rgba(255,255,255,0.03), rgba(0,0,0,0) 70%);
  }
  .brand {
    position: absolute;
    left: 0;
    right: 0;
    top: 190px;
    display: flex;
    justify-content: center;
    align-items: center;
    gap: 16px;
  }
  .brand-dot {
    width: 34px;
    height: 34px;
    border-radius: 50%;
    background: var(--brand-sky);
  }
  .brand-name {
    font-family: "Arimo", Arial, sans-serif;
    font-weight: 700;
    font-size: 62px;
    letter-spacing: 4px;
    color: var(--brand-sky);
    line-height: 1;
  }
  .tagline {
    position: absolute;
    left: 0;
    right: 0;
    top: 288px;
    text-align: center;
    font-family: "Open Sans", Arial, sans-serif;
    font-style: italic;
    font-size: 15px;
    color: var(--text-light);
    letter-spacing: 0.3px;
  }
  .contact {
    position: absolute;
    left: 0;
    right: 0;
    top: 456px;
    text-align: center;
    font-family: "Arimo", Arial, sans-serif;
    font-weight: 700;
    font-size: 26px;
    line-height: 32px;
    color: var(--text-light);
    text-shadow: 2px 3px 4px var(--text-shadow);
  }
  .contact p { margin: 0; }
  .contact .person-name {
    color: var(--name-red);
    text-shadow: -1px -1px 0 #fff, 1px -1px 0 #fff, -1px 1px 0 #fff, 1px 1px 0 #fff, 2px 3px 4px var(--text-shadow);
  }
</style>
</head>
<body>
<main class="canvas">
  <section class="card">
    <div class="card-texture" role="img" aria-label="Faint decorative background pattern"></div>
    <div class="brand">
      <span class="brand-dot"></span>
      <span class="brand-name">VORTIQ</span>
    </div>
    <p class="tagline">BOLD HORIZON SPORTS NUTRITION.</p>
    <div class="contact">
      <p class="person-name">Milo Harrow</p>
      <p class="role">CEO/Sport Nutrition Specialist</p>
      <p class="phone">Phone No.: 0473 628 904</p>
      <p class="email">Milo@vortiqfuelworks.example</p>
      <p class="website">www.vortiqfuelworks.example</p>
    </div>
  </section>
</main>
</body>
</html>
```